New landing page for book

Redesign http://www.kelvostramedia.com so it looks more cutting edge and perhaps have buttons for the online bookstores.

Also I may soon have a trailer video produced so it Would be great to see an option with space for where a video might go and an option as the site is now without a video. Thanks

Industry/Entity Type

Online

Number of Pages Required

1 page

Colors

Designer to choose colors to be used in the design.

```html
<!DOCTYPE html>
<html lang="en">
<head>
<meta charset="utf-8">
<title>Kravna — Dorian Valecroft</title>
<link rel="stylesheet" href="https://fonts.googleapis.com/css2?family=Oswald:wght@500;700&family=Roboto+Slab:wght@700;800&family=Open+Sans:wght@400;600;700&display=swap">
<style>
:root{
  --ink:#111214;
  --orange:#f07a1c;
  --orange-light:#ffa53a;
  --amber:#f5b53a;
  --bronze:#b7764a;
  --buy-brown:#8b6548;
  --teal:#2f5f55;
  --teal-light:#4e8577;
  --slate:#3a3d40;
  --body:#2b2b2b;
  --paper:#efefed;
  --card:#e3e4e5;
  --white:#ffffff;
}
*{box-sizing:border-box;margin:0;padding:0}
html,body{width:1200px;height:2946px;overflow:hidden}
body{position:relative;background:var(--ink);font-family:"Open Sans",Arial,sans-serif;color:var(--body)}
.abs{position:absolute}

/* Header / hero */
.hero{left:0;top:0;width:1200px;height:648px;background:radial-gradient(ellipse at 60% 40%,#34353a 0%,#1a1b1d 55%,#0c0c0d 100%)}
.brand{left:98px;top:18px;font-family:"Oswald",sans-serif;font-weight:700;font-size:56px;line-height:1;color:var(--orange);letter-spacing:1px}
.brand-author{left:160px;top:80px;font-family:"Oswald",sans-serif;font-weight:700;font-size:15px;color:var(--orange);letter-spacing:1px}
.nav{right:100px;top:32px;display:flex;gap:38px;font-family:"Oswald",sans-serif;font-weight:500;font-size:22px;color:var(--orange);letter-spacing:1px;text-transform:uppercase}
.nav .caret{font-size:12px;margin-left:6px;vertical-align:middle}
.genre{left:98px;top:160px;width:470px;font-family:"Oswald",sans-serif;font-weight:700;text-transform:uppercase;line-height:1}
.genre .line1{display:block;font-size:40px;color:var(--bronze)}
.genre .line2{display:block;font-size:64px;margin-top:8px;color:var(--amber)}
.hero-buy{left:98px;top:318px;font-family:"Roboto Slab",serif;font-weight:800;font-size:40px;line-height:1;color:var(--buy-brown);letter-spacing:2px}
.stores{left:98px;top:387px;display:grid;grid-template-columns:163px 198px;column-gap:14px;row-gap:15px}
.store{height:55px;border:2px solid #d9d9d9;border-radius:12px;background:#050505;display:flex;align-items:center;justify-content:center;gap:10px;color:var(--white);font-weight:600;font-size:20px}
.store .dot{width:16px;height:16px;border-radius:50%;background:var(--white)}
.hero-book{left:580px;top:100px;width:520px;height:540px;background:linear-gradient(135deg,#3b2b22 0%,#7a4a2a 30%,#2f5f55 65%,#e9ece8 100%);border-radius:4px}
.band{left:0;top:648px;width:1200px;height:79px;background:repeating-linear-gradient(135deg,#2c2d2f 0 4px,#1e1f21 4px 8px);border-bottom:3px solid #0d0d0e}

/* Story */
.story{left:0;top:727px;width:1200px;height:1149px;background:linear-gradient(180deg,#f4f4f2 0%,#e9e9e7 100%)}
.rule-head{left:0;width:1200px;display:flex;align-items:center;justify-content:center;gap:24px}
.story-head{top:820px}
.rule{width:210px;height:3px;background:var(--slate)}
.section-title{font-family:"Oswald",sans-serif;font-weight:700;font-size:58px;line-height:1;color:var(--slate);text-transform:uppercase}
.story-sub{left:0;top:892px;width:1200px;text-align:center;font-family:"Oswald",sans-serif;font-weight:700;font-size:40px;line-height:50px;color:var(--slate);text-transform:uppercase}
.pill{left:122px;top:1031px;width:954px;height:93px;border-radius:46px;background:linear-gradient(180deg,var(--teal-light),var(--teal));box-shadow:0 4px 8px rgba(0,0,0,.3);color:var(--white);font-weight:700;font-size:19px;line-height:25px;text-align:center;text-transform:uppercase;display:flex;align-items:center;justify-content:center;padding:0 60px}
.synopsis{left:150px;top:1158px;width:900px;text-align:center;font-size:17px;line-height:25px}
.synopsis p{margin-bottom:24px}
.pitch{left:122px;top:1484px;width:450px;font-family:"Oswald",sans-serif;font-weight:500;font-size:23px;line-height:33px;color:var(--teal)}
.btn-buy{width:370px;height:84px;border-radius:42px;background:linear-gradient(180deg,var(--orange-light),var(--orange));box-shadow:0 4px 8px rgba(0,0,0,.35);display:flex;align-items:center;justify-content:space-between;padding:0 14px 0 46px;font-family:"Roboto Slab",serif;font-weight:800;font-size:40px;color:var(--white)}
.btn-buy .cart{width:58px;height:58px;border-radius:50%;background:rgba(255,255,255,.18);display:flex;align-items:center;justify-content:center}
.story-btn{left:124px;top:1675px}
.trailer{left:600px;top:1469px;width:520px;height:334px;background:linear-gradient(135deg,#dcdcdc 0%,#2f3b38 20%,#2f5f55 55%,#8a4a24 80%,#d9d9d9 100%);border-radius:8px}
.divider{left:0;top:1876px;width:1200px;height:39px;background:repeating-linear-gradient(135deg,#2c2d2f 0 4px,#1e1f21 4px 8px)}

/* Reviews */
.reviews{left:0;top:1915px;width:1200px;height:481px;background:var(--paper)}
.reviews-head{top:1968px}
.reviews-kicker{left:0;top:2036px;width:1200px;text-align:center;font-size:14px;color:#666;letter-spacing:1px}
.card{top:2086px;width:310px;height:177px;background:var(--card);display:flex;align-items:center;justify-content:center;text-align:center;padding:20px 26px;font-size:14px;line-height:20px;color:#333}
.reviewer{top:2284px;display:flex;align-items:center;gap:18px;font-weight:700;font-size:17px;color:var(--orange);text-transform:uppercase}
.reviewer .avatar{width:58px;height:58px;border-radius:50%;background:linear-gradient(135deg,#9aa0a6,#4d5257);border:3px solid #fff}

/* Release */
.release{left:0;top:2396px;width:1200px;height:432px;background:radial-gradient(ellipse at 40% 40%,#2b2c2f 0%,#141516 70%)}
.release-word{left:118px;top:2440px;font-family:"Oswald",sans-serif;font-weight:700;font-size:142px;line-height:1;color:var(--bronze)}
.release-date{left:122px;top:2590px;font-family:"Oswald",sans-serif;font-weight:700;font-size:48px;line-height:1;color:var(--orange)}
.release-mail{left:124px;top:2652px;font-size:30px;color:var(--white)}
.release-btn{left:120px;top:2710px;width:362px;height:80px}
.release-book{left:726px;top:2362px;width:400px;height:446px;background:linear-gradient(135deg,#3b2b22 0%,#7a4a2a 35%,#2f5f55 70%,#e9ece8 100%);border-radius:4px}
.footer{left:0;top:2828px;width:1200px;height:118px;background:linear-gradient(180deg,#9a9a98,#5f5f5e);display:flex;align-items:center;justify-content:center;font-family:"Oswald",sans-serif;font-weight:500;font-size:26px;color:#111;text-transform:uppercase}
</style>
</head>
<body>

<header class="abs hero">
  <div class="abs brand">Kravna</div>
  <div class="abs brand-author">DORIAN VALECROFT</div>
  <nav class="abs nav"><span>Buy Now!<span class="caret">▼</span></span><span>Contact</span></nav>
  <h1 class="abs genre"><span class="line1">International Financial</span><span class="line2">Crime Thriller</span></h1>
  <div class="abs hero-buy">BUY NOW</div>
  <div class="abs stores">
    <div class="store"><span class="dot"></span>Bookvault</div>
    <div class="store">Hartley &amp; Finch</div>
    <div class="store"><span class="dot"></span>Pagestream</div>
    <div class="store"><span class="dot"></span>Leafshelf</div>
    <div class="store"><span class="dot"></span>Novarra</div>
    <div class="store"><span class="dot"></span>Inkwharf</div>
  </div>
  <div class="abs hero-book" role="img" aria-label="3D stack of Kravna hardcover books, cover showing an armed operative before the Capitol and a city skyline"></div>
</header>
<div class="abs band"></div>

<section class="abs story"></section>
<div class="abs rule-head story-head"><span class="rule"></span><h2 class="section-title">ATMs Have Shuttered.</h2><span class="rule"></span></div>
<p class="abs story-sub">Stock markets have gone haywire. Can one operative<br>stop a deadly band of criminals before it is too late?</p>
<div class="abs pill">When Anton Reisler is asked to investigate a devastating cyber-attack, he is drawn into a conspiracy that threatens not only his own life, but the entire United States' economy...</div>
<div class="abs synopsis">
  <p>German intelligence operative Anton Reisler has been asked to investigate the cyber crime gang who sparked massive unrest in Kenya by taking over electronic transactions. But as he digs deeper, a wiretap on hacker communications reveals this is only the beginning.</p>
  <p>Kravna, a shadowy criminal cabal, has launched a massive cyber attack on the United States.</p>
  <p>Taking off for Washington, Reisler unexpectedly teams up with American gun for hire, Miles Hartigan, and dives head-first into a massive conspiracy that reaches all the way up to the very top of the U.S. Government.</p>
  <p>Stock markets have gone haywire. ATMs have shuttered. And Anton Reisler is about to come face to face with the men he is sent to find....</p>
</div>
<p class="abs pitch">From the deadly streets of Budapest to the equally perilous corridors of Washington, Kravna is an action-packed, compulsive thriller that depicts a financial scam terrifyingly close to reality.</p>
<a class="abs btn-buy story-btn">BUY NOW<span class="cart"><svg width="34" height="30" viewBox="0 0 34 30"><path d="M2 3h6l4 16h16l4-11H10" fill="none" stroke="#fff" stroke-width="3" stroke-linejoin="round"/><circle cx="14" cy="25" r="2.6" fill="#fff"/><circle cx="26" cy="25" r="2.6" fill="#fff"/></svg></span></a>
<div class="abs trailer" role="img" aria-label="Book trailer video player shown on a laptop and phone, with the Kravna title over a teal brick wall"></div>
<div class="abs divider"></div>

<section class="abs reviews"></section>
<div class="abs rule-head reviews-head"><span class="rule"></span><h2 class="section-title">In the Words of Reviewers</h2><span class="rule"></span></div>
<div class="abs reviews-kicker">WHAT PEOPLE SAY</div>
<blockquote class="abs card" style="left:102px">"Valecroft's fast-paced novel is reinforced by its skilled characters"</blockquote>
<blockquote class="abs card" style="left:446px">"In a world ravaged by international turmoil and uncertainty for the future, author Dorian Valecroft presents Kravna, an intense and politically charged novel that is both timely and terrifying."</blockquote>
<blockquote class="abs card" style="left:790px">"I give Kravna by Dorian Valecroft a definite four out of four stars. The action is fast paced so that it keeps you wanting to see what comes next."</blockquote>
<div class="abs reviewer" style="left:102px"><span class="avatar"></span>Corvin Reviews</div>
<div class="abs reviewer" style="left:446px"><span class="avatar"></span>Reader</div>
<div class="abs reviewer" style="left:790px"><span class="avatar"></span>ShelfTalk Club</div>

<section class="abs release"></section>
<div class="abs release-word">RELEASED</div>
<div class="abs release-date">SEPTEMBER 22, 2017</div>
<div class="abs release-mail">help@kelvostramedia.com</div>
<a class="abs btn-buy release-btn">BUY NOW<span class="cart"><svg width="34" height="30" viewBox="0 0 34 30"><path d="M2 3h6l4 16h16l4-11H10" fill="none" stroke="#fff" stroke-width="3" stroke-linejoin="round"/><circle cx="14" cy="25" r="2.6" fill="#fff"/><circle cx="26" cy="25" r="2.6" fill="#fff"/></svg></span></a>
<div class="abs release-book" role="img" aria-label="3D stack of Kravna hardcover books"></div>

<footer class="abs footer">© Copyright 2017 Dorian Valecroft - All Rights Reserved</footer>

</body>
</html>
```